New Year Resolution Infographic

We are a weight loss company that provides holistic, natural nutrition programs to consumers -- you can see our Web site at www.TrimLark.com We need a simple infographic to be shared on social media and via email for New Year's day. The topic for the infographic is "how to set and keep your weight loss resolution". We've outlined 5 process steps for consumers to follow to assist with their weight loss resolutions, and we would like to depict this graphically.

Target Market(s)

Women age 35-65 who are planning to make a resolution to lose weight in the new year.

Industry/Entity Type

Health And Wellness

Font styles to use
Sans Serif

Colors
0392cd
9bcb3c

Requirements
Must have
• Initial graphic showing failure stats (see copy)
• Graphic showing process steps in making/keeping a resolution (see copy)
• TrimLark Logo

```html
<!DOCTYPE html>
<html lang="en">
<head>
<meta charset="utf-8">
<title>TrimLark – Weight Loss Resolution Infographic</title>
<link rel="stylesheet" href="https://fonts.googleapis.com/css2?family=Montserrat:wght@400;500;700;800&display=swap">
<style>
  :root{
    --blue:#0392cd;
    --blue-light:#d7ecf8;
    --blue-mid:#8ccbec;
    --green:#9bcb3c;
    --ink:#2b2b2b;
    --grey:#bdbdbd;
    --backdrop:#d1d2d4;
    --paper:#ffffff;
  }
  *{box-sizing:border-box;margin:0;padding:0}
  html,body{width:1200px;height:1200px;overflow:hidden;background:var(--backdrop);
    font-family:"Montserrat",Arial,sans-serif;color:var(--ink)}
  .flyer{position:absolute;left:355px;top:197px;width:612px;height:1008px;background:var(--paper);
    transform:scale(.8);transform-origin:0 0;overflow:hidden}
  .abs{position:absolute}
  .blue{color:var(--blue)} .green{color:var(--green)}
  b{font-weight:700}

  .header-block{left:0;top:30px;width:28px;height:37px;background:var(--blue)}
  .brand{left:34px;top:28px;display:flex;align-items:center;gap:10px;height:40px}
  .brand-dot{width:26px;height:26px;border-radius:50%;background:var(--green)}
  .brand-name{font-size:36px;font-weight:500;color:var(--blue);letter-spacing:-.5px}
  .url-ribbon{left:350px;top:30px;width:226px;height:37px}
  .url-text{left:350px;top:30px;width:200px;height:37px;line-height:37px;text-align:center;
    color:#fff;font-size:14px}

  .title-top{left:38px;top:100px;font-size:26px;font-weight:400;letter-spacing:.3px}
  .title-top b{color:var(--blue);font-weight:600}
  .title-band{left:8px;top:138px;width:500px;height:44px}
  .title-main{left:40px;top:138px;height:44px;line-height:44px;color:#fff;font-size:33px;font-weight:800;letter-spacing:.5px}
  .hero-badge{left:473px;top:101px;width:108px;height:108px;border-radius:50%;border:3px solid var(--green);background:#fff}
  .hero-art{left:16px;top:16px;width:70px;height:70px;border-radius:50%;
    background:linear-gradient(160deg,var(--blue) 0 45%,#4a4a4a 46% 100%);opacity:.85}

  .intro{left:37px;top:194px;font-size:14px;line-height:17px;letter-spacing:.3px}

  .stat-ring{left:114px;top:249px;width:112px;height:112px}
  .stat-art{left:149px;top:274px;width:56px;height:62px;border-radius:8px;
    background:linear-gradient(180deg,var(--blue) 0 55%,#3f3f3f 56% 100%)}
  .stat-copy{left:254px;top:268px;font-size:14px;line-height:17px;letter-spacing:.3px}
  .stat-copy b{font-weight:700}

  .guide-icon{left:36px;top:370px;width:56px;height:60px}
  .guide-copy{left:110px;top:384px;font-size:14px;line-height:17px;letter-spacing:.3px}
  .guide-rule{left:90px;top:426px;width:490px;height:6px}

  .step{font-size:12px;line-height:14.5px;letter-spacing:.3px}
  .step b{color:var(--blue);font-size:13.5px}
  .step-reflect{left:222px;top:440px;width:175px}
  .step-reward{left:34px;top:582px;width:160px}
  .step-resolve{left:426px;top:582px;width:165px}
  .step-record{left:126px;top:734px;width:185px}
  .step-replace{left:356px;top:736px;width:185px}

  .wheel{left:186px;top:512px;width:240px;height:230px}

  .footer{left:0;top:850px;width:612px;height:158px}
  .footer-copy{left:36px;top:902px;color:#fff;font-size:14.5px;line-height:17px;letter-spacing:.3px}
  .footer-copy p+p{margin-top:10px}
  .footer-copy .light{font-weight:400}
</style>
</head>
<body>
<main class="flyer">
  <div class="abs header-block"></div>
  <div class="abs brand"><span class="brand-dot"></span><span class="brand-name">TRIMLARK</span></div>
  <svg class="abs url-ribbon" viewBox="0 0 226 37"><polygon points="0,0 226,0 200,18.5 226,37 0,37" fill="#0392cd"/></svg>
  <div class="abs url-text">www.TrimLark.com</div>

  <h1 class="abs title-top">How to <b>SET</b> and <b>REACH</b> Your</h1>
  <svg class="abs title-band" viewBox="0 0 500 44"><polygon points="0,0 500,0 500,44 0,44 20,22" fill="#9bcb3c"/></svg>
  <h2 class="abs title-main">Weight Loss Resolution</h2>
  <div class="abs hero-badge"><div class="abs hero-art" role="img" aria-label="Illustration of a person walking on a treadmill"></div></div>

  <p class="abs intro"><b class="green">WEIGHT LOSS</b> is the <span class="blue">#1 New Year</span> resolution, but we know<br>that <b class="green">RESOLUTIONS</b> are very difficult to keep.</p>

  <svg class="abs stat-ring" viewBox="0 0 112 112">
    <circle cx="56" cy="56" r="50" fill="none" stroke="#bdbdbd" stroke-width="8"/>
    <path d="M100 34 A50 50 0 0 1 90 92" fill="none" stroke="#0392cd" stroke-width="8"/>
  </svg>
  <div class="abs stat-art" role="img" aria-label="Illustration of a person running on a treadmill"></div>
  <svg class="abs" style="left:176px;top:250px;width:140px;height:70px" viewBox="0 0 140 70">
    <circle cx="2.5" cy="3" r="2" fill="#fff" stroke="#888"/>
    <path d="M4 3 H131 V14 M126 14 H136" stroke="#888" fill="none"/>
    <path d="M46 59 H78 M78 54 V64" stroke="#888" fill="none"/>
  </svg>
  <p class="abs stat-copy">While <b class="green">45%</b> <b class="blue">OF AMERICANS</b> make<br>New Year <b class="green">RESOLUTIONS</b>, only<br><b class="blue">8% SUCCEED</b> in keeping<br>those resolutions.</p>

  <svg class="abs guide-icon" viewBox="0 0 56 60">
    <rect x="2" y="4" width="52" height="54" rx="3" fill="none" stroke="#9bcb3c" stroke-width="2"/>
    <path d="M2 12 H54 M10 4 V58" stroke="#9bcb3c" stroke-width="2"/>
    <circle cx="28" cy="30" r="10" fill="none" stroke="#0392cd" stroke-width="2.5"/>
    <path d="M35 37 L46 48" stroke="#0392cd" stroke-width="4" stroke-linecap="round"/>
  </svg>
  <p class="abs guide-copy">Here is a <b class="blue">QUICK GUIDE</b> to setting and reaching your<br><b class="green">WEIGHT LOSS</b> resolution this year.</p>
  <svg class="abs guide-rule" viewBox="0 0 490 6"><path d="M0 3 H484" stroke="#9bcb3c" stroke-width="2"/><circle cx="485" cy="3" r="3" fill="#9bcb3c"/></svg>

  <p class="abs step step-reflect"><b>REFLECT:</b> Get clear on why the achievement of your resolution is important. You'll need to come back to this if you falter!</p>
  <p class="abs step step-reward"><b>REWARD:</b> Rather than using unhealthy food as a reward or cheat, give yourself healthy or relaxing experiences – such a spa treatment or taking a new fitness class.</p>
  <p class="abs step step-resolve"><b>RESOLVE:</b> Set a weight loss goal for the year that is realistic, then break this up into even shorter term goals of 30-60 days, with a specific diet and activity plan to guide you.</p>
  <p class="abs step step-record"><b>RECORD:</b> Track your progress daily, tell your family and friends about your resolution to create more accountability, and recruit a partner to share your journey.</p>
  <p class="abs step step-replace"><b>REPLACE:</b> Clear out your pantry and stock up with only healthy foods. Then work to build new activity and eating habits that take the place of your current habits.</p>

  <svg class="abs wheel" viewBox="186 512 240 230" aria-label="Five-step cycle: reflect, resolve, replace, record, reward">
    <circle cx="306" cy="622" r="70" fill="#0392cd"/>
    <circle cx="306" cy="622" r="36" fill="#fff"/>
    <g fill="#d7ecf8" stroke="#fff" stroke-width="3">
      <circle cx="308" cy="566" r="29"/>
      <circle cx="370" cy="614" r="29"/>
      <circle cx="340" cy="690" r="29"/>
      <circle cx="262" cy="684" r="29"/>
      <circle cx="242" cy="610" r="29"/>
    </g>
    <g fill="#0392cd" opacity=".75">
      <rect x="296" y="556" width="24" height="22" rx="4"/>
      <rect x="360" y="602" width="20" height="24" rx="2"/>
      <circle cx="340" cy="692" r="11"/>
      <rect x="253" y="672" width="18" height="24" rx="2"/>
      <circle cx="242" cy="612" r="11"/>
    </g>
    <g fill="#0392cd">
      <polygon points="308,521 302,531 314,531"/>
      <polygon points="416,616 406,610 406,622"/>
      <polygon points="362,725 350,718 360,728"/>
      <polygon points="240,716 242,728 252,722"/>
      <polygon points="196,612 206,606 206,618"/>
    </g>
  </svg>

  <svg class="abs footer" viewBox="0 0 612 158" preserveAspectRatio="none">
    <defs><linearGradient id="sheen" x1="0" x2="1"><stop offset="0" stop-color="#ffffff"/><stop offset=".5" stop-color="#bdbdbd"/><stop offset="1" stop-color="#9a9a9a"/></linearGradient></defs>
    <path d="M0 22 Q260 -12 480 30 Q580 60 612 158 H0 Z" fill="url(#sheen)"/>
    <path d="M0 30 Q260 0 470 38 Q575 66 608 158 H0 Z" fill="#9bcb3c"/>
    <path d="M0 42 Q260 14 460 48 Q570 74 604 158 H0 Z" fill="#0392cd"/>
  </svg>
  <div class="abs footer-copy">
    <p><b>TRIMLARK</b> <span class="light">can help you achieve your</span><br><b>WEIGHT LOSS RESOLUTION</b> <span class="light">in the New Year.</span></p>
    <p>We invite you to learn more and<br>contact us for a <b>FREE CONSULTATION</b>.</p>
  </div>
</main>
</body>
</html>
```